Flyer Design Project for Sports Medicine Services

I am a sports medicine doctor specialising in the diagnosis and management of sport and exercise injuries for all ages and levels of activity - from elite to weekend jogger. I work under the Business name Peak Motion Athletic Care and do have a company logo. I am wanting a flier that I can send to family doctors, physiotherapists and sports clubs explaining who I am what I can offer and why they should send me patients.
- I have a Masters in Sports Medicine (MSportsMed), Diplomas in Obstetrics/Gynaecology (DRANZCOG) and also Paediatrics (DCH) and certificate in advanced clinical hypnosis
-accurate diagnosis and management plan with their regular physio to return the player / athlete to the field / court /gym as soon as safely possible
-hypnosis for sports performance eg anxiety control, confidence and mental rehearsal for individuals and teams
- because there are many possible therapists and therapy options, as a sports doctor I can work out who they need to see a physiotherapist, surgeon, massage therapist chiropractor or podiatrist to return them to activity or whether cortisone, PRP or autologous blood injections are needed
-can provide one point of contact for coaches and clubs for rehabilitation and return to sport advice.
- work with Clara Hutchings ex Australian Athlete, a Performance Strategist (NRC listed resource person) and registered Psychologist for best mental preparation for individuals teams and coach development
- can organise rapid access to MRI, ultrasound and specialist appointments if needed
-I work at 3 practices KineCore 418 Tolley Rd Marion 84619032 Monday Wednesday Friday; Harrow Lane Sports Clinic, 153 Denholm Rd, Adelaide 81764290 Tuesday Riverbend Falcons Sports Medicine Clinic, Norvale Park 8291 6475 Thursday.
-facebook site peakmotionathleticcare
Updates
Hi All, just to clarify.. My name is Paul Denton and I am the sports doctor. My wife is Clara Hutchings and she is the psychologist. The flier should mainly be advertising my sports medicine services and a byline ( or at least not the first line in the title) about the Performance Strategy and Coach development.
Target Market(s)
family doctors (GPs), Sporting Clubs, Physiotherapists
Industry/Entity Type
Massage
Look and feel

```html
<!DOCTYPE html>
<html lang="en">
<head>
<meta charset="utf-8">
<title>Peak Motion Athletic Care – Sports Medicine Flyer</title>
<link rel="stylesheet" href="https://fonts.googleapis.com/css2?family=Open+Sans:wght@300;400;600&family=Roboto+Condensed:wght@700&display=swap">
<style>
  :root {
    --paper: #ffffff;
    --heading-grey: #7d7d80;
    --body-grey: #4a4a4c;
    --footer-blue: #2a5b8c;
    --brand-blue: #1f6fb2;
    --hex-line: #e3e6ea;
  }
  * { margin: 0; padding: 0; box-sizing: border-box; }
  html, body { width: 839px; height: 1200px; overflow: hidden; background: var(--paper); }
  .flyer { position: relative; width: 839px; height: 1200px; background: var(--paper); font-family: "Open Sans", Arial, sans-serif; }

  .brand {
    position: absolute; top: 22px; left: 330px; width: 180px;
    display: flex; align-items: center; gap: 10px;
  }
  .brand-mark { width: 26px; height: 26px; border-radius: 50%; background: var(--brand-blue); flex: none; }
  .brand-name {
    font-family: "Open Sans", Arial, sans-serif; font-weight: 600;
    font-size: 17px; line-height: 1.15; color: var(--brand-blue);
  }

  .collage { position: absolute; top: 0; left: 0; width: 839px; height: 640px; }

  .intro { position: absolute; left: 336px; top: 655px; width: 440px; }
  .practitioners {
    font-weight: 300; font-size: 30px; line-height: 1.15; color: var(--heading-grey);
    margin-bottom: 24px;
  }
  .copy { font-size: 13.5px; line-height: 1.6; color: var(--body-grey); margin-bottom: 16px; }

  .locations {
    position: absolute; left: 120px; right: 80px; top: 1128px;
    font-family: "Roboto Condensed", "Arial Narrow", sans-serif; font-weight: 700;
    font-size: 15px; line-height: 1.3; color: var(--footer-blue); text-align: center;
  }
</style>
</head>
<body>
<main class="flyer">
  <svg class="collage" viewBox="0 0 839 640" xmlns="http://www.w3.org/2000/svg">
    <defs>
      <linearGradient id="tone-device" x1="0" y1="0" x2="1" y2="1">
        <stop offset="0" stop-color="#f2f2f0"/><stop offset="1" stop-color="#c9c6bf"/>
      </linearGradient>
      <linearGradient id="tone-track" x1="0" y1="0" x2="0" y2="1">
        <stop offset="0" stop-color="#b4553e"/><stop offset="1" stop-color="#7a2f22"/>
      </linearGradient>
      <linearGradient id="tone-xray" x1="0" y1="0" x2="1" y2="1">
        <stop offset="0" stop-color="#5a6068"/><stop offset="1" stop-color="#141618"/>
      </linearGradient>
      <linearGradient id="tone-doctor" x1="0" y1="0" x2="1" y2="1">
        <stop offset="0" stop-color="#8fb8dc"/><stop offset="0.6" stop-color="#c9dff0"/><stop offset="1" stop-color="#eef4fa"/>
      </linearGradient>
    </defs>

    <g class="hex-outlines" fill="none" stroke="var(--hex-line)" stroke-width="2">
      <polygon points="560,20 620,55 620,125 560,160 500,125 500,55"/>
      <polygon points="40,440 100,475 100,545 40,580 -20,545 -20,475"/>
      <polygon points="420,470 470,499 470,556 420,585 370,556 370,499"/>
    </g>

    <polygon role="img" aria-label="Photo: portable medical monitoring device on a white strap"
      fill="url(#tone-device)" points="120,145 241,215 241,355 120,425 -1,355 -1,215"/>
    <polygon role="img" aria-label="Photo: athlete's running shoes on a red running track"
      fill="url(#tone-track)" points="385,160 498,225 498,355 385,420 272,355 272,225"/>
    <polygon role="img" aria-label="Photo: x-ray of a knee joint"
      fill="url(#tone-xray)" points="240,380 348,442 348,567 240,630 132,567 132,442"/>
    <polygon role="img" aria-label="Photo: doctor in blue scrubs holding a clipboard and stethoscope"
      fill="url(#tone-doctor)" points="680,100 897,225 897,475 680,600 463,475 463,225"/>
  </svg>

  <header class="brand">
    <span class="brand-mark"></span>
    <span class="brand-name">Peak Motion<br>Athletic Care</span>
  </header>

  <section class="intro">
    <h1 class="practitioners">Paul Denton / Sport doctor<br>Clara Hutchings / Psychologist</h1>
    <p class="copy">Lorem ipsum dolor sit amet, consectetur adipiscing elit. Vestibulum justo sem, bibendum nec varius vulputate, vulputate nec velit. Ut malesuada tempor pretium. Vestibulum ante ipsum primis in faucibus orci luctus et ultrices posuere cubilia curae. Donec ut lacus ut dui fringilla blandit nec ac lorem. Quisque tincidunt sapien ac augue egestas nec bibendum tellus aliquam. Nunc nisl lacus, iaculis at consequat sit amet, dapibus vel tortor. Nunc euismod rhoncus pharetra. Aenean pretium turpis tristique senectus et netus et malesuada fames ac turpis egestas.</p>
    <p class="copy">Nulla lacinia eleifend ligula, sed convallis mi luctus at. Duis non tortor nisi. Donec feugiat quis erat magna adipiscing placerat lacinia nisi tincidunt. Etiam a mi sit amet dui volutpat tempor a vel elit. Duis mauris libero, tincidunt vehicula venenatis sit amet, rhoncus id nunc. Suspendisse est nulla, sodales sed lacinia vitae, vestibulum ac felis. Pellentesque a diam erat, a bibendum eros.</p>
  </section>

  <footer class="locations">
    KineCore 418 Tolley Rd Marion 84619032 Monday Wednesday Friday<br>
    Harrow Lane Sports Clinic, 153 Denholm Rd, Adelaide 81764290 Tuesday<br>
    Riverbend Falcons Sports Medicine Clinic, Norvale Park 8291 6475 Thursday.
  </footer>
</main>
</body>
</html>
```